CoinLantern one-page corporate website

Our company, CoinLantern is a cryptocurrency Initial Coin Offering ("ICO" marketing and promotion agency, which requires a professional company landing page design whereby prospective clients can learn;
-who we are
-what we do
-what our people are saying about us
-core team members
-subscribe to our mailing list
-how to get in touch (basic contact form)

We are looking for something unique and attractive -- not a standard Vanto template that we could put together ourselves. Plain stock images should not be used. Unique visualizations of the service offerings and creative presentation are key. We are a cutting edge marketing agency and as such, we need to look the part.

Relevant documentation about the business and branding assets have been attached to guide the designer. Certain information will be included by the company at a later date such as team member descriptions. As such, lorem ipsum may be included wherever necessary to help visualize the textual areas.

****Please ensure that you actually utilize the photos and graphics provided so that we can have a good picture of what it would actually look like with our branding.

The site must be responsive HTML CSS Design.

Sites style themes we like for inspiration and specific sections we like ****Very important***:
https://fundrivermesh.com/offers - we like that the token & company logo is used in unique visualizations that connects various ideas together. We imagine unique visuals such as these with our Icon (see attached) serving as a token. We also like the unique and attractive visual theme of the webpage itself.

https://pavoniaholdings.com/ - we like the layout of this website, specifically how the service offerings are displayed in a circular visual graphic with the Pavonia logo in the middle. We imagine a similar type of graphic designed with CoinLantern in the middle.

https://quorvanet.org/ - we like how the logo is central to the theme in this site when you first enter and how it fades + shrinks into the distance as you scroll down.

Target Market(s)

cryptocurrency entrepreneurs and ICOs

Industry/Entity Type

It Company

Coding

Coded - Design and coding required

Number of Pages Required

1 page

Font styles to use
Sans Serif

Colors

Designer to choose colors to be used in the design.

Requirements
Must have
• The site must be responsive HTML CSS Design.
• The page must be modern and visually attractive. Elements must not be static and should have a fluid motion / visual change as the user scrolls through the page.
Should not have
• The project should not use any old stock images or elements which are dull and over-used, but rather images or elements should be unique and well thought out.

```html
<!DOCTYPE html>
<html lang="en">
<head>
<meta charset="utf-8">
<title>CoinLantern – End-to-End ICO Capital Raising Solution</title>
<link href="https://fonts.googleapis.com/css2?family=Quicksand:wght@400;500;600;700&family=Tinos:ital,wght@0,400;0,700;1,400&display=swap" rel="stylesheet">
<style>
:root{
  --purple:#6a5ae6;
  --blue:#3f9fe8;
  --cyan:#4fcfe6;
  --navy:#1d3b6b;
  --band:#1f3a5c;
  --ink:#2b2b2b;
  --muted:#6b7280;
  --line:#1e4d8c;
  --pale:#dff4fb;
  --white:#ffffff;
  --grad:linear-gradient(90deg,var(--purple) 0%,#5a86ea 55%,var(--cyan) 100%);
}
*{box-sizing:border-box;margin:0;padding:0}
html,body{width:1200px;height:4945px;overflow:hidden}
body{position:relative;background:var(--white);font-family:'Tinos',Georgia,serif;color:var(--ink)}
.abs{position:absolute}
.heading{font-family:'Quicksand',Arial,sans-serif;font-weight:500}
/* header */
.site-header{position:absolute;left:0;top:0;width:1200px;height:92px;background:var(--white);display:flex;align-items:center;padding:0 100px}
.brand{display:flex;align-items:center;gap:10px;font-family:'Quicksand',Arial,sans-serif;font-weight:700;font-size:30px;color:var(--blue)}
.brand-dot{width:38px;height:38px;border-radius:50%;border:3px solid var(--blue)}
.main-nav{margin-left:auto;display:flex;gap:30px;font-size:15px;color:var(--ink);align-items:center}
.btn{display:inline-flex;align-items:center;justify-content:center;border-radius:20px;font-family:'Tinos',Georgia,serif;color:var(--white);font-size:15px}
.btn-join{background:var(--blue);width:90px;height:36px;margin-left:10px}
/* hero */
.hero{position:absolute;left:0;top:92px;width:1200px;height:680px;background:var(--grad)}
.hero-title{position:absolute;left:100px;top:128px;color:var(--white);font-size:40px;line-height:48px;font-weight:500}
.hero-text{position:absolute;left:100px;top:236px;width:620px;color:var(--white);font-size:15px;line-height:22px}
.btn-read{position:absolute;left:100px;top:310px;width:110px;height:34px;background:var(--navy)}
.alerts-title{position:absolute;left:0;top:440px;width:1200px;text-align:center;color:var(--white);font-size:22px;letter-spacing:.5px}
.alerts-form{position:absolute;left:400px;top:495px;display:flex;gap:14px}
.field{background:var(--white);border-radius:20px;height:42px;padding:0 18px;display:flex;align-items:center;color:#999;font-size:14px}
.btn-signup{width:125px;height:42px;border:2px solid rgba(255,255,255,.7);background:rgba(255,255,255,.15);border-radius:21px}
/* what we do */
.section-title{position:absolute;left:0;width:1200px;text-align:center;font-size:32px;color:var(--navy)}
.service-label{position:absolute;font-family:'Quicksand',Arial,sans-serif;font-weight:500;font-size:19px;line-height:24px;color:var(--ink)}
.btn-pill{position:absolute;height:38px;background:var(--blue);border-radius:19px}
/* who */
.who-text{position:absolute;left:100px;width:560px;color:var(--white);font-size:16px;line-height:24px}
.who-title{position:absolute;left:100px;color:var(--white);font-size:34px}
/* steps */
.step-label{position:absolute;width:200px;text-align:center;font-family:'Quicksand',Arial,sans-serif;font-size:20px;line-height:24px;color:var(--ink)}
.step-label.blue{color:var(--blue)}
/* testimonials */
.quote-card{position:absolute;top:2795px;width:225px;height:290px;border:2px solid rgba(255,255,255,.85);padding:20px 18px;color:var(--white)}
.quote-mark{font-family:'Tinos',Georgia,serif;font-size:64px;line-height:40px;font-weight:700}
.stars{position:absolute;right:18px;top:26px;font-size:16px;letter-spacing:2px}
.quote-text{margin-top:20px;font-family:'Quicksand',Arial,sans-serif;font-size:13px;line-height:19px}
.quote-name{position:absolute;right:18px;bottom:16px;font-size:11px;font-family:'Quicksand',Arial,sans-serif}
/* contact list */
.social-row{position:absolute;left:760px;width:350px;height:56px;background:#f2f4f7;padding:9px 14px;font-family:'Quicksand',Arial,sans-serif}
.social-name{font-size:14px;font-weight:700;color:var(--ink)}
.social-sub{font-size:12px;color:var(--muted)}
.social-mark{position:absolute;right:14px;top:14px;width:28px;height:28px;border-radius:4px}
/* team */
.team-card{position:absolute;top:3850px;width:322px;height:320px;border:2px solid var(--navy);border-radius:6px;padding:80px 24px 0;text-align:center}
.avatar{position:absolute;left:50%;top:-58px;margin-left:-56px;width:112px;height:112px;border-radius:50%;border:4px solid var(--white);box-shadow:0 0 0 2px var(--navy);background:linear-gradient(160deg,#c9a58a,#3b4a6b)}
.team-name{font-family:'Quicksand',Arial,sans-serif;font-weight:600;font-size:17px}
.team-role{font-style:italic;font-size:15px;color:var(--ink);margin:4px 0 10px}
.team-bio{font-size:15px;line-height:20px;text-align:left}
/* subscribe */
.subscribe{position:absolute;left:0;top:4320px;width:1200px;height:130px;background:var(--band)}
/* message */
.message{position:absolute;left:0;top:4450px;width:1200px;height:430px;background:var(--grad)}
.box{position:absolute;background:var(--white);color:#999;font-size:13px;padding:8px 12px}
footer{position:absolute;left:0;top:4880px;width:1200px;height:65px;text-align:center;padding-top:30px;font-size:12px;color:var(--muted)}
.to-top{position:absolute;left:578px;top:-22px;width:44px;height:44px;border-radius:50%;background:var(--navy)}
</style>
</head>
<body>

<header class="site-header">
  <div class="brand"><span class="brand-dot"></span>CoinLantern</div>
  <nav class="main-nav">
    <span>Home</span><span>How Does It Work</span><span>What We Do</span><span>Testimonials</span><span>Our Team</span><span>Contact</span>
    <span class="btn btn-join">Join Us</span>
  </nav>
</header>

<section class="hero">
  <svg class="abs" style="left:0;top:0" width="1200" height="680" aria-hidden="true">
    <path d="M0 680 L0 600 Q600 720 1200 560 L1200 680 Z" fill="rgba(255,255,255,.06)"/>
  </svg>
  <h1 class="hero-title heading">End-to-End ICO Capital<br>Raising Solution</h1>
  <p class="hero-text">The only technology first investment bank licensed exclusively on the digital finance sector – the emerging crypto currency and token based capital markets.</p>
  <span class="btn btn-read">Read More</span>
  <h2 class="alerts-title heading">SIGN UP FOR ICO NEWS &amp; ALERTS</h2>
  <div class="alerts-form">
    <div class="field" style="width:260px">Your Email</div>
    <span class="btn btn-signup">SIGN UP</span>
  </div>
</section>

<!-- what we do -->
<svg class="abs" style="left:0;top:740px" width="1200" height="60" aria-hidden="true">
  <path d="M0 30 Q600 -20 1200 20 L1200 60 L0 60 Z" fill="#fff"/>
</svg>
<h2 class="section-title heading" style="top:796px">What we do</h2>
<svg class="abs" style="left:0;top:850px" width="1200" height="520" aria-hidden="true">
  <g fill="none" stroke="var(--line)" stroke-width="3">
    <path d="M420 60 A225 225 0 0 0 420 420"/>
    <path d="M780 60 A225 225 0 0 1 780 420" stroke="var(--blue)"/>
    <polyline points="175,30 400,30 430,68"/>
    <polyline points="175,205 350,205 378,212"/>
    <polyline points="175,355 380,355 405,380"/>
    <polyline points="1070,30 800,30 775,68" stroke="var(--blue)"/>
    <polyline points="1070,180 860,180 822,212" stroke="var(--blue)"/>
    <polyline points="1070,380 820,380 800,380" stroke="var(--blue)"/>
  </g>
  <circle cx="600" cy="240" r="120" fill="none" stroke="var(--line)" stroke-width="3"/>
  <circle cx="600" cy="240" r="100" fill="#e8f6fc" role="img" aria-label="CoinLantern token emblem"/>
  <g fill="var(--navy)">
    <circle cx="445" cy="90" r="40"/><circle cx="390" cy="230" r="40"/><circle cx="440" cy="395" r="40"/>
  </g>
  <g fill="var(--blue)">
    <circle cx="755" cy="90" r="40"/><circle cx="815" cy="235" r="40"/><circle cx="760" cy="395" r="40"/>
  </g>
  <g fill="none" stroke="#fff" stroke-width="3">
    <rect x="430" y="74" width="28" height="32" rx="2"/><line x1="436" y1="84" x2="452" y2="84"/><line x1="436" y1="92" x2="452" y2="92"/>
    <rect x="378" y="218" width="24" height="24" transform="rotate(45 390 230)"/>
    <rect x="426" y="381" width="28" height="28"/><line x1="440" y1="385" x2="440" y2="405"/>
    <circle cx="755" cy="90" r="14"/><path d="M749 90 l5 5 l8 -10"/>
    <rect x="799" y="223" width="32" height="22" rx="2"/><line x1="810" y1="250" x2="820" y2="250"/>
    <path d="M746 402 l8 -12 l8 6 l10 -14"/>
  </g>
</svg>
<div class="service-label" style="left:175px;top:852px">Whitepaper Consultation<br>and Review</div>
<div class="service-label" style="left:175px;top:1027px">Token sale strategy</div>
<div class="service-label" style="left:175px;top:1155px">Raise amount &amp; future<br>token price strategy</div>
<div class="service-label" style="left:820px;top:852px;width:250px;text-align:right">KYC (Know Your Customer)<br>strategies</div>
<div class="service-label" style="left:820px;top:1003px;width:250px;text-align:right">Secure Token Launch<br>Website</div>
<div class="service-label" style="left:820px;top:1203px;width:250px;text-align:right">Marketing Representation</div>

<!-- who are you -->
<svg class="abs" style="left:0;top:1330px" width="1200" height="800" aria-hidden="true">
  <defs>
    <linearGradient id="whoGrad" x1="0" x2="1" y1="0" y2="0">
      <stop offset="0" stop-color="#6a5ae6"/><stop offset=".55" stop-color="#5a86ea"/><stop offset="1" stop-color="#4fcfe6"/>
    </linearGradient>
  </defs>
  <path d="M0 80 Q300 130 650 100 Q950 70 1200 0 L1200 650 Q700 690 0 780 Z" fill="url(#whoGrad)"/>
  <path d="M0 780 Q700 690 1200 650 L1200 690 Q700 720 0 800 Z" fill="var(--navy)"/>
</svg>
<span class="btn btn-pill" style="left:522px;top:1371px;width:156px">View More Services</span>
<h2 class="who-title heading" style="top:1520px">Who are you?</h2>
<p class="who-text" style="top:1574px">We are a group of global experts connected through a cutting edge Decentralized Organizational structure powered by Smart Contracts. We have no employees – just owners. That is why your success is our shared mission.</p>
<div class="abs" style="left:100px;top:1705px;width:560px;border-top:2px dashed rgba(255,255,255,.6)"></div>
<h2 class="who-title heading" style="top:1735px">How much does it cost?</h2>
<p class="who-text" style="top:1790px">Every Token sale is unique, that is why CoinLantern begins with a one-on-one conversation to identify your specific needs and agree upon terms that make sense for all parties. We structure engagements according to the principle of aligned interests - our success is your success and vice versa.</p>

<!-- how does it work -->
<h2 class="section-title heading" style="top:2160px;color:var(--ink);font-size:30px">How does it work?</h2>
<svg class="abs" style="left:0;top:2230px" width="1200" height="300" aria-hidden="true">
  <path d="M80 140 L175 140 Q270 140 270 200 Q270 140 365 140 Q460 140 460 90 Q460 140 560 140 Q710 140 710 200 Q710 140 860 140 Q975 140 975 90 Q975 140 1120 140" fill="none" stroke="#45b6ea" stroke-width="30" stroke-linecap="round"/>
  <g fill="var(--pale)" stroke="#bfe6f5" stroke-width="2">
    <circle cx="270" cy="180" r="62"/><circle cx="460" cy="100" r="62"/><circle cx="710" cy="180" r="62"/><circle cx="975" cy="100" r="62"/>
  </g>
  <g fill="none" stroke="var(--navy)" stroke-width="3">
    <rect x="252" y="158" width="36" height="44" rx="3"/><line x1="260" y1="172" x2="280" y2="172"/><line x1="260" y1="182" x2="280" y2="182"/>
    <rect x="440" y="78" width="40" height="28" rx="3"/><circle cx="460" cy="120" r="7"/><path d="M445 138 q15 -14 30 0"/>
    <rect x="692" y="158" width="34" height="44" rx="3"/><path d="M700 190 l14 -14 l6 6 l-14 14 z"/>
    <circle cx="975" cy="100" r="20"/><circle cx="975" cy="100" r="6" fill="var(--navy)"/>
  </g>
</svg>
<div class="step-label" style="left:360px;top:2230px">Conference Call<br>with Expert</div>
<div class="step-label" style="left:875px;top:2232px">Let the<br>Magic Begin</div>
<div class="step-label blue" style="left:125px;top:2478px;width:200px;text-align:left;padding-left:48px">Submit<br>Application</div>
<div class="step-label blue" style="left:610px;top:2478px">Sign<br>Agreement</div>

<!-- testimonials -->
<section class="abs" style="left:0;top:2637px;width:1200px;height:528px;background:var(--grad)">
  <h2 class="section-title heading" style="top:50px;color:#fff;font-size:30px">What our people are saying about us</h2>
</section>
<article class="quote-card" style="left:190px">
  <div class="quote-mark">“</div><div class="stars">★★★★★</div>
  <p class="quote-text">Lorem Ipsum is simply dummy text of the printing and typesetting industry. Lorem Ipsum has been the industry's standard dummy text ever since the 1500s. When an unknown printer took a galley of type and scrambled it to make a type specimen book.</p>
  <div class="quote-name">– NAME HERE</div>
</article>
<article class="quote-card" style="left:488px">
  <div class="quote-mark">“</div><div class="stars">★★★★★</div>
  <p class="quote-text">Lorem Ipsum is simply dummy text of the printing and typesetting industry. Lorem Ipsum has been the industry's standard dummy text ever since the 1500s. When an unknown printer took a galley of type and scrambled it to make a type specimen book.</p>
  <div class="quote-name">– NAME HERE</div>
</article>
<article class="quote-card" style="left:785px">
  <div class="quote-mark">“</div><div class="stars">★★★★★</div>
  <p class="quote-text">Lorem Ipsum is simply dummy text of the printing and typesetting industry. Lorem Ipsum has been the industry's standard dummy text ever since the 1500s. When an unknown printer took a galley of type and scrambled it to make a type specimen book.</p>
  <div class="quote-name">– NAME HERE</div>
</article>

<!-- video & contact -->
<h2 class="abs heading" style="left:100px;top:3228px;font-size:30px">Watch Video</h2>
<div class="abs" style="left:100px;top:3300px;width:560px;height:290px;border:4px solid var(--blue);background:linear-gradient(135deg,#b9c6dc,#7f8fb3)" role="img" aria-label="Video preview explaining the CoinLantern token process"></div>
<div class="abs" style="left:348px;top:3398px;width:64px;height:64px;border-radius:50%;background:rgba(255,255,255,.9)"></div>
<svg class="abs" style="left:370px;top:3415px" width="26" height="30" aria-hidden="true"><path d="M0 0 L26 15 L0 30 Z" fill="var(--navy)"/></svg>
<div class="abs" style="left:104px;top:3556px;width:552px;height:30px;background:rgba(20,25,40,.85)"></div>
<div class="abs" style="left:150px;top:3569px;width:380px;height:4px;background:#7a8396"></div>
<div class="abs" style="left:150px;top:3569px;width:130px;height:4px;background:#fff"></div>

<h2 class="abs heading" style="left:760px;top:3228px;font-size:30px">Get In Touch</h2>
<div class="social-row" style="top:3300px"><div class="social-name">FRIENDWALL</div><div class="social-sub">Like us on Friendwall</div><span class="social-mark" style="background:#3b5998"></span></div>
<div class="social-row" style="top:3366px"><div class="social-name" style="color:#d93025">CLIPSTREAM</div><div class="social-sub">Subscribe on Clipstream</div><span class="social-mark" style="background:#e53935"></span></div>
<div class="social-row" style="top:3432px"><div class="social-name" style="color:#2aa3ef">CHIRPER</div><div class="social-sub">Follow us on Chirper</div><span class="social-mark" style="background:#2aa3ef"></span></div>
<div class="social-row" style="top:3498px"><div class="social-name">PROLINKED</div><div class="social-sub">Connect with us on ProLinked</div><span class="social-mark" style="background:#0a66c2"></span></div>
<div class="social-row" style="top:3564px"><div class="social-name">THREADBOARD</div><div class="social-sub">Join us on Threadboard</div><span class="social-mark" style="background:#333"></span></div>

<!-- team -->
<h2 class="section-title heading" style="top:3718px;font-size:30px">Core Team Members</h2>
<article class="team-card" style="left:100px">
  <div class="avatar" role="img" aria-label="Portrait of Dorian Velasko"></div>
  <div class="team-name">Dorian Velasko</div><div class="team-role">Director</div>
  <p class="team-bio">Lorem Ipsum is simply dummy text of the printing and typesetting industry. Lorem Ipsum has been the industry's standard dummy text ever since the 1500s, when an unknown printer took a galley of type and scrambled it to make a type specimen book.</p>
</article>
<article class="team-card" style="left:440px">
  <div class="avatar" role="img" aria-label="Portrait of Marcus Fennley"></div>
  <div class="team-name">Marcus Fennley</div><div class="team-role">Technical advisor</div>
  <p class="team-bio">Lorem Ipsum is simply dummy text of the printing and typesetting industry. Lorem Ipsum has been the industry's standard dummy text ever since the 1500s, when an unknown printer took a galley of type and scrambled it to make a type specimen book.</p>
</article>
<article class="team-card" style="left:780px">
  <div class="avatar" role="img" aria-label="Portrait of Anurak Solvanich"></div>
  <div class="team-name">Anurak Solvanich</div><div class="team-role">Marketing Consultant</div>
  <p class="team-bio">Lorem Ipsum is simply dummy text of the printing and typesetting industry. Lorem Ipsum has been the industry's standard dummy text ever since the 1500s, when an unknown printer took a galley of type and scrambled it to make a type specimen book.</p>
</article>
<span class="btn btn-pill" style="left:522px;top:4200px;width:156px">View More</span>

<!-- subscribe -->
<section class="subscribe">
  <h2 class="abs heading" style="left:148px;top:44px;font-size:30px;color:#fff">Subscribe to our mailing list</h2>
  <div class="field abs" style="left:580px;top:40px;width:480px;height:50px;border-radius:25px">Your Email</div>
  <div class="abs" style="left:1012px;top:47px;width:36px;height:36px;border-radius:50%;background:var(--purple)"></div>
  <svg class="abs" style="left:1020px;top:55px" width="20" height="20" aria-hidden="true"><path d="M3 10 H16 M10 4 L16 10 L10 16" stroke="#fff" stroke-width="3" fill="none"/></svg>
</section>

<!-- message -->
<section class="message">
  <h2 class="section-title heading" style="top:34px;color:#fff;font-size:30px">Send Us A Message</h2>
  <p class="abs" style="left:330px;top:90px;width:540px;text-align:center;color:#fff;font-size:14px;line-height:19px">Lorem Ipsum is simply dummy text of the printing and typesetting industry. Lorem Ipsum has been the industry's standard dummy text ever since the 1500s.</p>
  <div class="box" style="left:160px;top:168px;width:385px;height:160px">Message</div>
  <div class="box" style="left:620px;top:168px;width:430px;height:40px">Name</div>
  <div class="box" style="left:620px;top:226px;width:430px;height:40px">Email</div>
  <div class="box" style="left:620px;top:286px;width:240px;height:40px">Type the code shown</div>
  <div class="box" style="left:862px;top:286px;width:48px;height:40px;color:var(--ink);font-weight:700">H6345</div>
  <span class="btn abs" style="left:920px;top:286px;width:130px;height:40px;border:2px solid rgba(255,255,255,.8)">Send Message</span>
</section>

<footer>
  <span class="to-top"></span>
  <svg class="abs" style="left:589px;top:-12px" width="22" height="22" aria-hidden="true"><path d="M4 15 L11 8 L18 15" stroke="#fff" stroke-width="3" fill="none"/></svg>
  Copyright © 2017 CoinLantern. All rights reserved.
</footer>

</body>
</html>
```